PPT Design Project for an educational startup

We seek a PPT design for a new company based in Japan called "Brivorent".
We provide PPT slide-based educational videos for free.
Please see the link below. You will see some videos.
http://velmora-example.jp/
The current template is also attached.
As we are changing our service name from Velmora to Brivorent, we are considering to change the PPT template as well.
Here are some notes regarding this project.
1. We need three pages;
- Title page: Letters for the tile and the logo are necessary. Some pictorial marks or other design would be appreciated.
- Contents page: Just one line to divide the message part and contents part should be sufficient. Please do not spend your time here.
- Final page: The word "Thank you for watching!" in the center. Some pictorial marks or other design would be appreciated.
2. Please use light green, orange, and purple as main colors. (Same as the current template)
3. You don't have to think about the font-style. This is going to be Japanese font, so we will take care of this.
4. Background color needs to be white, as the slides could be printed out.
5. We use Powerpoint for Mac.
6. No copyright section required, as these slides will be creative commons. Instead of the copyright section, please put the creative commons mark in all slides. (which is in the original template attached)
Updates
Please forget about the creative commons mark.
Hi all,
Target Market(s)
16-25 years old people, who are highly educated or highly motivated for education
Industry/Entity Type
It Company
Requirements
Must have
- 1. Creative commons mark (which is in the original template)
Should not have
- 1. Copyright mark

```html
<!DOCTYPE html>
<html lang="en">
<head>
<meta charset="utf-8">
<title>Brivorent – Presentation Template</title>
<link rel="stylesheet" href="https://fonts.googleapis.com/css2?family=Source+Sans+3:wght@400;600;700&family=Arvo:wght@700&display=swap">
<style>
  :root {
    --stage: #f1efec;
    --slide: #ffffff;
    --ink: #5f6062;
    --ink-soft: #6f7072;
    --rule: #9a9b9d;
    --footer: #8a8b8d;
    --green: #7cbb2c;
    --orange: #f29a1d;
    --red: #e2342a;
    --purple: #8a4fa8;
    --tab-text: #ffffff;
  }
  * { box-sizing: border-box; margin: 0; padding: 0; }
  html, body { width: 1200px; height: 647px; overflow: hidden; }
  body {
    background: var(--stage);
    font-family: "Source Sans 3", Arial, sans-serif;
    color: var(--ink);
    position: relative;
  }
  .slide {
    position: absolute;
    width: 309px;
    height: 232px;
    background: var(--slide);
    overflow: hidden;
    box-shadow: 0 2px 6px rgba(0,0,0,.18);
  }
  .slide--title   { left: 89px;  top: 69px; }
  .slide--list    { left: 442px; top: 67px; }
  .slide--text    { left: 791px; top: 67px; }
  .slide--bullets { left: 255px; top: 358px; }
  .slide--closing { left: 613px; top: 358px; }

  .slide__swoosh { position: absolute; inset: 0; }

  .slide__footer { position: absolute; left: 0; bottom: 0; width: 309px; height: 34px; }
  .slide__url {
    position: absolute; right: 48px; bottom: 5px;
    font-size: 7px; font-weight: 700; color: #ffffff; letter-spacing: .3px;
  }
  .slide__badge {
    position: absolute; right: 8px; bottom: 4px;
    width: 24px; height: 24px; border-radius: 50%;
    background: #ffffff; border: 3px solid var(--footer);
  }

  .slide__heading {
    position: absolute; left: 22px; top: 8px;
    font-size: 13.5px; font-weight: 700; color: var(--ink-soft);
  }
  .slide__rule {
    position: absolute; left: 18px; right: 0; top: 27px;
    height: 1px; background: var(--rule);
  }

  .body-text {
    font-size: 6.3px; line-height: 9.4px; color: var(--ink);
    text-align: justify; hyphens: auto;
  }

  /* Title slide */
  .brand-name {
    position: absolute; left: 0; right: 0; text-align: center;
    font-weight: 700; color: var(--green); letter-spacing: -.5px;
  }
  .slide--title .brand-name { top: 26px; font-size: 42px; }
  .presentation-title {
    position: absolute; left: 0; right: 0; top: 93px; text-align: center;
    font-size: 19px; font-weight: 400; color: var(--orange);
  }
  .hero-art {
    position: absolute; left: 30px; top: 137px; width: 235px; height: 80px;
    border-radius: 40px 40px 8px 8px;
    background: linear-gradient(90deg, #d23a2e, #f08a24, #f2c21b, #6cb33f, #2f9bd0, #3f5fb0, #8a4fa8, #c04a9a);
    opacity: .85;
  }

  /* Numbered list slide */
  .step { position: absolute; left: 8px; width: 122px; height: 41px; }
  .step--one   { top: 36px; }
  .step--two   { top: 95px; }
  .step--three { top: 154px; }
  .step__tab {
    position: absolute; inset: 0;
    clip-path: polygon(10% 0, 100% 0, 100% 100%, 10% 100%, 0 50%);
    border-radius: 4px;
  }
  .step--one .step__tab   { background: linear-gradient(#ef4a3c, #c8241b); }
  .step--two .step__tab   { background: linear-gradient(#fbb12e, #ea8a10); }
  .step--three .step__tab { background: linear-gradient(#9ccd3a, #6aa61f); }
  .step__num {
    position: absolute; left: 18px; top: 7px;
    font-size: 22px; font-weight: 600; color: var(--tab-text);
  }
  .step__divider { position: absolute; left: 45px; top: 8px; width: 1px; height: 25px; background: rgba(255,255,255,.8); }
  .step__note {
    position: absolute; left: 50px; top: 10px;
    font-size: 4.6px; line-height: 6px; font-weight: 600; color: var(--tab-text);
  }
  .list-copy { position: absolute; left: 139px; width: 151px; }
  .list-copy--one   { top: 33px; }
  .list-copy--two   { top: 92px; }
  .list-copy--three { top: 151px; }

  /* Full text slide */
  .text-column { position: absolute; left: 21px; right: 22px; top: 33px; }
  .text-column p + p { margin-top: 1px; }

  /* Bullet slide */
  .slide--bullets .text-column { left: 18px; right: 18px; }
  .bullet-list {
    position: absolute; left: 18px; top: 147px; list-style: none;
    font-size: 6.6px; font-weight: 700; color: var(--ink);
  }
  .bullet-list li { height: 13.4px; display: flex; align-items: center; gap: 6px; }
  .bullet-list li::before {
    content: ""; width: 5px; height: 5px; border-radius: 50%;
    background: radial-gradient(circle at 35% 35%, #9a9b9d, #3d3e40);
  }
  .learn-art {
    position: absolute; left: 144px; top: 132px; width: 158px; height: 70px;
    border-radius: 50% 50% 10px 10px / 70% 70% 10px 10px;
    background: linear-gradient(90deg, #e2342a, #f29a1d, #f2c21b, #7cbb2c, #2f9bd0, #8a4fa8);
    opacity: .8;
  }

  /* Closing slide */
  .slide--closing .brand-name { top: 32px; font-size: 40px; }
  .thanks {
    position: absolute; left: 0; right: 0; top: 144px; text-align: center;
    font-family: "Arvo", Georgia, serif; font-weight: 700;
    font-size: 22px; color: var(--green);
  }
  .thanks__sub {
    position: absolute; left: 0; right: 0; top: 172px; text-align: center;
    font-size: 12.5px; font-weight: 700; color: var(--orange);
  }
</style>
</head>
<body>

<!-- Slide 1: title -->
<section class="slide slide--title">
  <svg class="slide__swoosh" viewBox="0 0 309 232" aria-hidden="true">
    <path d="M0 60 C90 20 200 70 309 30" fill="none" stroke="#f3eee0" stroke-width="10"/>
  </svg>
  <div class="brand-name">Brivorent</div>
  <div class="presentation-title">Presentation Title</div>
  <div class="hero-art" role="img" aria-label="Row of colourful cartoon figures holding hands"></div>
  <svg class="slide__footer" viewBox="0 0 309 34" aria-hidden="true">
    <path d="M0 20 C80 8 170 8 309 14 L309 34 L0 34 Z" fill="var(--footer)"/>
    <path d="M0 18 C80 4 170 4 309 11" fill="none" stroke="var(--green)" stroke-width="2.5"/>
  </svg>
  <span class="slide__url">www.kelvaro-example.net</span>
  <span class="slide__badge"></span>
</section>

<!-- Slide 2: numbered list -->
<section class="slide slide--list">
  <h2 class="slide__heading">Lorem Ipsum</h2>
  <div class="slide__rule"></div>

  <div class="step step--one">
    <div class="step__tab"></div>
    <span class="step__num">01</span><span class="step__divider"></span>
    <p class="step__note">Plan your study<br>Set clear goals<br>Track progress daily</p>
  </div>
  <div class="step step--two">
    <div class="step__tab"></div>
    <span class="step__num">02</span><span class="step__divider"></span>
    <p class="step__note">Watch each lesson<br>Take short notes<br>Review key ideas</p>
  </div>
  <div class="step step--three">
    <div class="step__tab"></div>
    <span class="step__num">03</span><span class="step__divider"></span>
    <p class="step__note">Practice with quizzes<br>Share with friends<br>Keep learning</p>
  </div>

  <p class="body-text list-copy list-copy--one">Lorem ipsum dolor sit amet, consectetuer adipiscing elit, sed diam nonummy nibh euismod tincidunt ut laoreet dolore magna aliquam erat volutpat. Ut wisi enim ad minim veniam, quis nostrud exerci tation ullamcorper suscipit lobortis.</p>
  <p class="body-text list-copy list-copy--two">Lorem ipsum dolor sit amet, consectetuer adipiscing elit, sed diam nonummy nibh euismod tincidunt ut laoreet dolore magna aliquam erat volutpat. Ut wisi enim ad minim veniam, quis nostrud exerci tation ullamcorper suscipit lobortis.</p>
  <p class="body-text list-copy list-copy--three">Lorem ipsum dolor sit amet, consectetuer adipiscing elit, sed diam nonummy nibh euismod tincidunt ut laoreet dolore magna aliquam erat volutpat. Ut wisi enim ad minim veniam, quis nostrud exerci tation ullamcorper suscipit lobortis.</p>

  <svg class="slide__footer" viewBox="0 0 309 34" aria-hidden="true">
    <path d="M0 20 C80 8 170 8 309 14 L309 34 L0 34 Z" fill="var(--footer)"/>
    <path d="M0 18 C80 4 170 4 309 11" fill="none" stroke="var(--green)" stroke-width="2.5"/>
  </svg>
  <span class="slide__url">www.kelvaro-example.net</span>
  <span class="slide__badge"></span>
</section>

<!-- Slide 3: text -->
<section class="slide slide--text">
  <h2 class="slide__heading">Lorem Ipsum</h2>
  <div class="slide__rule"></div>
  <div class="text-column">
    <p class="body-text">Lorem ipsum dolor sit amet, consectetuer adipiscing elit, sed diam nonummy nibh euismod tincidunt ut laoreet dolore magna aliquam erat volutpat. Ut wisi enim ad minim veniam, quis nostrud exerci tation ullamcorper suscipit lobortis nisl ut aliquip ex ea commodo consequat.</p>
    <p class="body-text">Lorem ipsum dolor sit amet, consectetuer adipiscing elit, sed diam nonummy nibh euismod tincidunt ut laoreet dolore magna aliquam erat volutpat. Ut wisi enim ad minim veniam, quis nostrud exerci tation ullamcorper suscipit lobortis nisl ut aliquip ex ea commodo consequat. Duis autem vel eum iriure dolor in hendrerit in vulputate velit esse molestie consequat, vel illum dolore eu feugiat nulla facilisis.</p>
    <p class="body-text">Lorem ipsum dolor sit amet, consectetuer adipiscing elit, sed diam nonummy nibh euismod tincidunt ut laoreet dolore magna aliquam erat volutpat. Ut wisi enim ad minim veniam, quis nostrud exerci tation ullamcorper suscipit lobortis nisl ut aliquip ex ea commodo consequat. Duis autem vel eum iriure dolor in hendrerit in vulputate velit esse molestie consequat, vel illum dolore eu feugiat nulla facilisis.</p>
  </div>
  <svg class="slide__footer" viewBox="0 0 309 34" aria-hidden="true">
    <path d="M0 20 C80 8 170 8 309 14 L309 34 L0 34 Z" fill="var(--footer)"/>
    <path d="M0 18 C80 4 170 4 309 11" fill="none" stroke="var(--green)" stroke-width="2.5"/>
  </svg>
  <span class="slide__url">www.kelvaro-example.net</span>
  <span class="slide__badge"></span>
</section>

<!-- Slide 4: text with bullets -->
<section class="slide slide--bullets">
  <h2 class="slide__heading">Lorem Ipsum</h2>
  <div class="slide__rule"></div>
  <div class="text-column">
    <p class="body-text">Lorem ipsum dolor sit amet, consectetuer adipiscing elit, sed diam nonummy nibh euismod tincidunt ut laoreet dolore magna aliquam erat volutpat. Ut wisi enim ad minim veniam, quis nostrud exerci tation ullamcorper suscipit lobortis nisl ut aliquip ex ea commodo consequat. Duis autem vel eum iriure dolor in hendrerit in vulputate velit esse molestie consequat, vel illum dolore eu feugiat nulla facilisis.</p>
    <p class="body-text">Lorem ipsum dolor sit amet, consectetuer adipiscing elit, sed diam nonummy nibh euismod tincidunt ut laoreet dolore magna aliquam erat volutpat. Ut wisi enim ad minim veniam, quis nostrud exerci tation ullamcorper suscipit lobortis nisl ut aliquip ex ea commodo consequat. Duis autem vel eum iriure dolor in hendrerit in vulputate velit esse molestie consequat, vel illum dolore eu feugiat nulla facilisis.</p>
  </div>
  <ul class="bullet-list">
    <li>Lorem ipsum&nbsp; Lorem Lorem ipsum</li>
    <li>Lorem ipsum Lorem Lorem</li>
    <li>Lorem ipsum Lorem Lorem ipsum</li>
    <li>Lorem ipsum orem Lorem ipsum</li>
  </ul>
  <div class="learn-art" role="img" aria-label="Circle of colourful cartoon figures around the word Learn"></div>
  <svg class="slide__footer" viewBox="0 0 309 34" aria-hidden="true">
    <path d="M0 20 C80 8 170 8 309 14 L309 34 L0 34 Z" fill="var(--footer)"/>
    <path d="M0 18 C80 4 170 4 309 11" fill="none" stroke="var(--green)" stroke-width="2.5"/>
  </svg>
  <span class="slide__url">www.kelvaro-example.net</span>
  <span class="slide__badge"></span>
</section>

<!-- Slide 5: closing -->
<section class="slide slide--closing">
  <svg class="slide__swoosh" viewBox="0 0 309 232" aria-hidden="true">
    <path d="M0 70 C90 30 200 80 309 40" fill="none" stroke="#f3eee0" stroke-width="10"/>
  </svg>
  <div class="brand-name">Brivorent</div>
  <div class="thanks">Thank You!</div>
  <div class="thanks__sub">for watching!</div>
  <svg class="slide__footer" viewBox="0 0 309 34" aria-hidden="true">
    <path d="M0 20 C80 8 170 8 309 14 L309 34 L0 34 Z" fill="var(--footer)"/>
    <path d="M0 18 C80 4 170 4 309 11" fill="none" stroke="var(--green)" stroke-width="2.5"/>
  </svg>
  <span class="slide__url">www.kelvaro-example.net</span>
  <span class="slide__badge"></span>
</section>

</body>
</html>
```